Thank you for shopping with us business card

We would like a thank you card for our rebranded business. We used to be "Kestrel Knacks" but are now "Kestrel Trinkets. Old thank you card and new logo will be attached for reference. New thank you card does not have to be same design as old thank you card, but please use new logo.
Mopsa URL is now kestreltrinkets.mopsa.com
Pictaloo is @Kestrel_Trinkets
Email is kestreltrinkets@mopsamail.com
Thank you!

Contact Information for Business Card

Mopsa site, email, Pictaloo

```html
<!DOCTYPE html>
<html lang="en">
<head>
<meta charset="utf-8">
<title>Kestrel Trinkets – Thank You Card</title>
<link rel="stylesheet" href="https://fonts.googleapis.com/css2?family=Montserrat:wght@400;500;700;800&display=swap">
<style>
  :root {
    --page-bg: #3a3a3a;
    --card-bg: #1b1b1b;
    --card-bg-light: #2a2a2a;
    --ink-light: #ffffff;
    --ink-dark: #141414;
    --rule: #6a6a6a;
    --band: #ffffff;
  }
  * { box-sizing: border-box; margin: 0; padding: 0; }
  html, body {
    width: 1200px; height: 1200px; overflow: hidden;
    background: var(--page-bg);
    font-family: "Montserrat", sans-serif;
  }
  .stage {
    width: 1200px; height: 1200px;
    display: flex; align-items: center; justify-content: center;
  }
  .thanks-card {
    position: relative;
    width: 1000px; height: 636px;
    border-radius: 44px;
    background: var(--card-bg);
    overflow: hidden;
    box-shadow: 0 20px 50px rgba(0,0,0,.45);
  }
  .card-texture {
    position: absolute; inset: 0;
    background: radial-gradient(ellipse at 55% 45%, var(--card-bg-light) 0%, var(--card-bg) 70%);
  }
  .brand-block {
    position: absolute; left: 190px; top: 95px;
    display: flex; align-items: center; gap: 34px;
    color: var(--ink-light);
  }
  .brand-dot {
    width: 110px; height: 110px; border-radius: 50%;
    background: var(--ink-light);
  }
  .brand-divider {
    width: 2px; height: 150px; background: var(--ink-light);
  }
  .brand-name {
    font-weight: 700; font-size: 40px; line-height: 1.05;
    text-transform: uppercase; letter-spacing: .5px;
  }
  .thanks-band {
    position: absolute; left: 0; right: 0; top: 290px; height: 70px;
    background: var(--band);
    display: flex; align-items: center; justify-content: center;
  }
  .thanks-title {
    font-weight: 800; font-size: 36px; color: var(--ink-dark);
    text-transform: uppercase; letter-spacing: .5px;
  }
  .thanks-message {
    position: absolute; left: 330px; top: 385px;
    color: var(--ink-light); font-weight: 500; font-size: 34px; line-height: 1.3;
  }
  .contact-rule {
    position: absolute; left: 90px; right: 90px; top: 530px;
    height: 1px; background: var(--rule);
  }
  .contact-row {
    position: absolute; left: 0; right: 0; top: 555px;
    display: flex; justify-content: center; gap: 42px;
    color: var(--ink-light); font-size: 19px; font-weight: 400;
  }
  .contact-item { display: flex; align-items: center; gap: 10px; }
  .contact-icon {
    width: 24px; height: 24px; border-radius: 50%;
    background: var(--ink-light); flex: none;
    display: flex; align-items: center; justify-content: center;
  }
</style>
</head>
<body>
<main class="stage">
  <article class="thanks-card">
    <div class="card-texture" role="img" aria-label="Faint repeating brand pattern across the dark card"></div>

    <header class="brand-block">
      <span class="brand-dot" aria-hidden="true"></span>
      <span class="brand-divider" aria-hidden="true"></span>
      <h1 class="brand-name">Kestrel<br>Trinkets</h1>
    </header>

    <div class="thanks-band">
      <h2 class="thanks-title">Thank you for your purchase!</h2>
    </div>

    <p class="thanks-message">
      Your purchase made my day and I<br>
      hope this package brightens yours.<br>
      Please come back and leave a review!
    </p>

    <div class="contact-rule"></div>

    <ul class="contact-row">
      <li class="contact-item"><span class="contact-icon" aria-label="Mopsa"></span>kestreltrinkets.mopsa.com</li>
      <li class="contact-item"><span class="contact-icon" aria-label="Pictaloo"></span>@Kestrel_Trinkets</li>
      <li class="contact-item">
        <span class="contact-icon" aria-label="Email">
          <svg width="14" height="10" viewBox="0 0 14 10"><rect x="0.5" y="0.5" width="13" height="9" fill="none" stroke="#141414" stroke-width="1.2"/><path d="M0.5 0.5 L7 5.5 L13.5 0.5" fill="none" stroke="#141414" stroke-width="1.2"/></svg>
        </span>kestreltrinkets@mopsamail.com
      </li>
    </ul>
  </article>
</main>
</body>
</html>
```